Glenvora pond linings website template

We need a template for our new website. Glenvora is currently marketed through www.sheetvale.com.au, and we are moving the pond/dam linings to a dedicated site www.glenvora.com.au

The site is essentially brochureware. The content (less landing page & photo gallery) is on the new site to give you a better idea of what we do. We are also on Facebook.com/glenvora

We are looking for a template/style which we can adapt to the different sections of the site as required. We also get a lot of phone/tablet visitors so an alternative mobile layout would be a bonus, but by no means required.

I am proficient in HTML/CSS & javascript so can code most designs thrown at me.

Any icons or interface fonts should be freely available web fonts where possible.

Target Market(s)

We are targeting both landscape professionals (design & construction) as well as the DIY market for ponds/wateragrdens.

Industry/Entity Type

Moving

Requirements
Must have
• We need a design (preferably layered PSD or AI) as basis for our overall site look and feel. Fonts/iconography/layout are where we are lacking. We can do the HTML/CSS/JS/PHP internally.
Nice to have
• A style guide either in file or separate would be nice.
Layers with effect (i.e.. :hover, CSS3 transition endpoints, etc)

```html
<!DOCTYPE html>
<html lang="en">
<head>
<meta charset="utf-8">
<title>Glenvora – Custom made liners</title>
<link rel="stylesheet" href="https://fonts.googleapis.com/css2?family=PT+Sans+Narrow:wght@400;700&display=swap">
<style>
:root{
  --green:#6a9a2a;
  --green-dark:#4f7d1c;
  --orange:#d4782c;
  --text:#3a3a3a;
  --muted:#666;
  --line:#d8d8d8;
  --page:#f6f4f4;
  --white:#fff;
}
*{box-sizing:border-box;margin:0;padding:0}
html,body{width:874px;height:1200px;overflow:hidden}
body{font-family:"PT Sans Narrow",sans-serif;color:var(--text);background:var(--white);position:relative;font-size:10.5px;line-height:1.3}
.abs{position:absolute}
.site-header{position:absolute;left:0;top:0;width:874px;height:87px;border-top:1px solid var(--line);border-bottom:1px solid var(--line);background:var(--white)}
.brand{position:absolute;left:103px;top:22px;display:flex;align-items:center;gap:8px}
.brand-mark{width:30px;height:30px;background:var(--green)}
.brand-name{font-size:28px;color:var(--green);letter-spacing:1px;line-height:1}
.follow{position:absolute;left:509px;top:35px;font-size:10.5px;display:flex;align-items:center;gap:5px}
.social{width:20px;height:20px;border-radius:5px;background:var(--orange);display:inline-block}
.divider{width:1px;height:12px;background:#aaa;margin-left:8px}
.search{position:absolute;left:622px;top:29px;width:151px;height:28px;border:1px solid #bbb;font-size:10.5px;padding:7px 6px;color:#444}
.search svg{position:absolute;right:8px;top:7px}
.nav{position:absolute;left:103px;top:87px;height:34px;display:flex}
.nav a{display:flex;align-items:center;justify-content:center;height:34px;font-size:10.5px;color:var(--text);text-decoration:none;border-right:1px solid var(--line)}
.nav a.active{background:var(--green);color:var(--white)}
.hero{position:absolute;left:0;top:121px;width:874px;height:321px;background:linear-gradient(180deg,#4d6a38 0%,#6f7f5a 35%,#7e8a6e 62%,#c98a4e 82%,#e3964e 100%)}
.caption{position:absolute;left:103px;color:var(--white);font-size:24px;padding:0 12px;line-height:38px;height:38px}
.cap-1{top:116px;background:rgba(106,154,42,.9)}
.cap-2{top:155px;background:rgba(212,120,44,.9)}
.dots{position:absolute;left:103px;top:203px;display:flex;gap:2px}
.dots span{width:8px;height:8px;background:#bbb}
.dots span:first-child{background:var(--white)}
.content{position:absolute;left:0;top:442px;width:874px;height:681px;background:var(--page)}
.card{position:absolute;width:208px;height:221px;background:var(--white);border:1px solid #cfcfcf;box-shadow:0 0 2px rgba(0,0,0,.1);padding:6px}
.card .photo{width:194px;height:113px}
.card h3{font-weight:400;font-size:13px;color:var(--green);margin:9px 0 3px;text-transform:uppercase}
.card p{font-size:10px;line-height:1.25}
.btn{display:inline-block;background:var(--green);color:var(--white);font-size:10.5px;padding:3px 9px;margin-top:10px}
.section-title{font-size:13px;color:var(--green);font-weight:400;text-transform:uppercase}
.about{position:absolute;left:103px;top:514px;width:436px}
.about .head{display:flex;align-items:center;gap:6px}
.about .head i{flex:1;border-top:2px dotted #ccc}
.about p{font-size:10px;margin-top:10px;line-height:1.28}
.sidebar{position:absolute;left:562px;top:28px;width:211px}
.email{margin-top:6px;height:23px;background:#e8e8e8;border:1px solid #bbb;font-size:10px;padding:5px 6px}
.submit{margin-top:9px;display:inline-block;background:var(--green);color:var(--white);font-size:10.5px;padding:3px 16px}
.post{display:flex;gap:8px;padding:8px 0 8px;border-bottom:1px dashed #bbb}
.avatar{width:50px;height:50px;flex:none;border:2px solid var(--white);box-shadow:0 0 2px rgba(0,0,0,.3)}
.post p{font-size:10px;line-height:1.25}
.post .more{color:var(--green);font-size:9px}
.contacts p{font-size:10px;line-height:1.3}
.contacts em{color:var(--green)}
.footer{position:absolute;left:0;top:1123px;width:874px;height:76px;border-top:1px solid #ccc;border-bottom:1px solid #ccc;background:var(--white)}
.footer p{position:absolute;left:103px;top:33px;font-size:9.5px;color:#444}
</style>
</head>
<body>
<header class="site-header">
  <div class="brand"><span class="brand-mark"></span><span class="brand-name">GLENVORA</span></div>
  <div class="follow">Follow Us : <span class="social" aria-label="Social profile"></span><span class="social" aria-label="Blog"></span><span class="divider"></span></div>
  <div class="search">Search here...
    <svg width="14" height="14" viewBox="0 0 14 14"><circle cx="6" cy="6" r="4.5" fill="none" stroke="#888" stroke-width="1.4"/><line x1="9.3" y1="9.3" x2="13" y2="13" stroke="#888" stroke-width="1.6"/></svg>
  </div>
</header>

<nav class="nav">
  <a class="active" style="width:80px">Home</a>
  <a style="width:84px">About Us</a>
  <a style="width:95px">Happenings</a>
  <a style="width:71px">Gallery</a>
  <a style="width:80px">Liner Styles</a>
  <a style="width:83px">Preparation</a>
  <a style="width:77px">Installation</a>
  <a style="width:88px">Contact Us</a>
</nav>

<section class="hero" role="img" aria-label="Photo of a garden pond with waterfall, ferns and timber deck">
  <div class="caption cap-1">Custom made liners</div>
  <div class="caption cap-2">for ponds, pools &amp; watergardens</div>
  <div class="dots"><span></span><span></span><span></span></div>
</section>

<main class="content">
  <article class="card" style="left:103px;top:30px">
    <div class="photo" role="img" aria-label="Photo of a stone path beside a pond" style="background:linear-gradient(135deg,#5c6b58,#8a8f8c 45%,#5a3b3a)"></div>
    <h3>Flat Sheet Liners</h3>
    <p>Lorem ipsum dolor sit amet, consectetur adipisicing elit, sed do eiusmod tempor incididunt ut labore et dolore magna aliqua.</p>
    <span class="btn">Read More</span>
  </article>
  <article class="card" style="left:330px;top:30px">
    <div class="photo" role="img" aria-label="Photo of a pond with a curved timber edge" style="background:linear-gradient(180deg,#7c8a5a,#9a4a3c 50%,#3a3d2a)"></div>
    <h3>Composite Liners</h3>
    <p>Lorem ipsum dolor sit amet, consectetur adipisicing elit, sed do eiusmod tempor incididunt ut labore et dolore magna aliqua.</p>
    <span class="btn">Read More</span>
  </article>
  <article class="card" style="left:103px;top:271px">
    <div class="photo" role="img" aria-label="Photo of an excavated pond site lined with sand" style="background:linear-gradient(180deg,#3f5a30,#b8a77a 55%,#8c7d58)"></div>
    <h3>Profite Liners</h3>
    <p>Lorem ipsum dolor sit amet, consectetur adipisicing elit, sed do eiusmod tempor incididunt ut labore et dolore magna aliqua.</p>
    <span class="btn">Read More</span>
  </article>
  <article class="card" style="left:330px;top:271px">
    <div class="photo" role="img" aria-label="Photo of a rocky pond among tree ferns" style="background:linear-gradient(180deg,#4e6a3a,#6f7766 50%,#2f3a2c)"></div>
    <h3>Special Project Liners</h3>
    <p>Lorem ipsum dolor sit amet, consectetur adipisicing elit, sed do eiusmod tempor incididunt ut labore et dolore magna aliqua.</p>
    <span class="btn">Read More</span>
  </article>

  <section class="about">
    <div class="head"><h2 class="section-title">About Us</h2><i></i></div>
    <p>Glenvora has been manufactured, marketed and installed throughout Australia and the Pacific Rim since the early 1980's for a variety of domestic and commercial applications.</p>
    <p>Glenvora pond liners put an end to the complicated and time consuming installation used by other methods. Simply excavate or construct the desired shape of your pond pool or water garden, indoor or outdoor, place your Glenvora into position and secure the edges. It can easily be completed in a weekend. Glenvora pond liners are long lasting, economical to install and completely maintenance free.</p>
    <span class="btn" style="margin-top:14px">Read More</span>
  </section>

  <aside class="sidebar">
    <h2 class="section-title">Subscribe Us</h2>
    <div class="email">Your Email Id</div>
    <span class="submit">Submit</span>

    <h2 class="section-title" style="margin-top:14px">Our Blog</h2>
    <div class="post"><div class="avatar" role="img" aria-label="Author portrait" style="background:#b08a6a"></div><div><p>Lorem ipsum dolor sit amet, consectetur adipisicing elit, sed do eiusmod tempor incididunt ut labore et dolore magna.</p><span class="more">More &gt;</span></div></div>
    <div class="post"><div class="avatar" role="img" aria-label="Author portrait" style="background:#8fa6a0"></div><div><p>Lorem ipsum dolor sit amet, consectetur adipisicing elit, sed do eiusmod tempor incididunt ut labore et dolore magna.</p><span class="more">More &gt;</span></div></div>
    <div class="post"><div class="avatar" role="img" aria-label="Author portrait" style="background:#9a6a5a"></div><div><p>Lorem ipsum dolor sit amet, consectetur adipisicing elit, sed do eiusmod tempor incididunt ut labore et dolore magna.</p><span class="more">More &gt;</span></div></div>
    <div class="post" style="border-bottom:none"><div class="avatar" role="img" aria-label="Author portrait" style="background:#a0604a"></div><div><p>Lorem ipsum dolor sit amet, consectetur adipisicing elit, sed do eiusmod tempor incididunt ut labore et dolore magna.</p><span class="more">More &gt;</span></div></div>

    <div class="contacts" style="margin-top:12px">
      <h2 class="section-title" style="padding-bottom:6px;border-bottom:2px dotted #ccc">Contacts Us</h2>
      <p style="margin-top:8px">Postal :</p>
      <p><em>Factory1</em></p>
      <p>PO Box 2210, Harlow Ridge, Victoria, 3390, Australia</p>
      <p style="margin-top:12px"><em>Factory 2</em></p>
      <p>4-8 Tarrin Court, Westmere, Victoria, 3390, Australia</p>
      <p style="margin-top:14px">Phone : 1300 555 010</p>
      <p>International Phone : +61 3 9555 0142</p>
      <p>Fax : 1300 555 027</p>
      <p>International Fax : +61 3 9555</p>
      <p>eMail : support@glenvora.com</p>
    </div>
  </aside>
</main>

<footer class="footer">
  <p>Copyright@2013, glenvora.com &nbsp;|&nbsp; All rights are reserved.</p>
</footer>
</body>
</html>
```